Design a business card & stationary for a mortgage company

We are looking for a good looking business card design for our mortgage company that includes our logo. We received a free design as part of our logo project but we don't love it. The company is called "Birchfield Mortgage Company" so we like waves and lighthouses. The logo should be included. We have a version in both vertical and horizontal that we have provided.

Industry/Entity Type

Finance

Contact Information for Business Card

This should include our new logo file

Requirements
Must have
• 3. The details you'd like on the card - name, title, phone, email, website, address, social media handles etc.
1. Dennis Marlow
Vice President
614-390-2751
Fax 877-402-6158
dmarlow@birchfieldmortgage.example
NMLS 47192 - Company NMLS 62304
18 Elm Ave
Alder Bay, NJ 08512

```html
<!DOCTYPE html>
<html lang="en">
<head>
<meta charset="utf-8">
<title>Birchfield Mortgage Company – Business Card</title>
<link rel="stylesheet" href="https://fonts.googleapis.com/css2?family=Josefin+Sans:wght@400;600&family=Source+Sans+3:wght@400;700&display=swap">
<style>
  :root {
    --bg: #e4e5e7;
    --blue-bright: #0a93dc;
    --blue-mid: #0677c2;
    --blue-deep: #135a98;
    --navy: #1b3f78;
    --accent: #1f78c8;
    --ink: #3b3f45;
    --white: #ffffff;
  }
  * { margin: 0; padding: 0; box-sizing: border-box; }
  html, body { width: 1200px; height: 900px; overflow: hidden; }
  body { background: var(--bg); position: relative; font-family: "Source Sans 3", sans-serif; }

  .card {
    position: absolute;
    top: 217px;
    width: 309px;
    height: 500px;
    box-shadow: 2px 3px 6px rgba(0,0,0,.35);
  }
  .card-front {
    left: 279px;
    border-radius: 0 54px 0 54px;
    background: linear-gradient(160deg, var(--blue-deep) 0%, var(--blue-bright) 40%, var(--blue-mid) 70%, var(--blue-deep) 100%);
    color: var(--white);
    text-align: center;
  }
  .card-back {
    left: 617px;
    border-radius: 54px 0 54px 0;
    background: var(--white);
  }

  .wordmark { position: absolute; left: 0; right: 0; text-align: center; font-family: "Josefin Sans", sans-serif; font-weight: 400; }
  .wordmark .mark-dot { display: block; margin: 0 auto 16px; border-radius: 50%; width: 44px; height: 44px; }
  .wordmark .name { display: block; font-size: 27px; line-height: 1.15; letter-spacing: 1px; }
  .card-front .wordmark { top: 170px; color: var(--white); }
  .card-front .mark-dot { background: var(--white); }
  .card-back .wordmark { top: 85px; color: var(--navy); }
  .card-back .mark-dot { background: var(--navy); }

  .licenses { position: absolute; top: 427px; left: 0; right: 0; font-size: 14.5px; line-height: 18px; }

  .person { position: absolute; left: 30px; top: 300px; }
  .person-name { font-weight: 700; font-size: 21px; color: var(--navy); letter-spacing: .2px; line-height: 22px; }
  .person-title { font-size: 14.5px; color: var(--accent); line-height: 18px; }

  .contacts { position: absolute; left: 30px; top: 354px; list-style: none; font-size: 14px; color: var(--ink); }
  .contacts li { display: flex; align-items: center; height: 18px; white-space: nowrap; }
  .contacts svg { width: 13px; height: 13px; margin-right: 6px; fill: var(--navy); flex: none; }
  .contacts svg.icon-globe { fill: none; stroke: var(--navy); stroke-width: 1.4; }
  .contacts .web-host { color: var(--navy); }
  .contacts .address { margin-top: 11px; }
  .contacts .address svg { width: 12px; height: 16px; margin-right: 10px; margin-left: 2px; }
</style>
</head>
<body>

<section class="card card-front" aria-label="Card front">
  <div class="wordmark">
    <span class="mark-dot"></span>
    <span class="name">Birchfield<br>Mortgage Company</span>
  </div>
  <p class="licenses">NMLS 47192<br>Company NMLS 62304</p>
</section>

<section class="card card-back" aria-label="Card back">
  <div class="wordmark">
    <span class="mark-dot"></span>
    <span class="name">Birchfield<br>Mortgage Company</span>
  </div>

  <div class="person">
    <p class="person-name">DENNIS MARLOW</p>
    <p class="person-title">VICE PRESIDENT</p>
  </div>

  <ul class="contacts">
    <li>
      <svg viewBox="0 0 16 16"><path d="M3.5 1l2.5 3-1.5 2c.8 2 2.5 3.7 4.5 4.5l2-1.5 3 2.5-1.5 2.5C7 14 2 9 1 2.5z"/></svg>
      614-390-2751
    </li>
    <li>
      <svg viewBox="0 0 16 16"><path d="M4 1h8v4H4zM1 6h14v6h-3v3H4v-3H1zM5 10v4h6v-4z" fill-rule="evenodd"/></svg>
      877-402-6158
    </li>
    <li>
      <svg viewBox="0 0 16 16"><path d="M1 3h14v10H1zM2.5 4.5v.4L8 9l5.5-4.1v-.4zM2.5 6.6v5h11v-5L8 10.8z" fill-rule="evenodd"/></svg>
      dmarlow@birchfieldmortgage.example
    </li>
    <li>
      <svg class="icon-globe" viewBox="0 0 16 16"><circle cx="8" cy="8" r="6.5"/><ellipse cx="8" cy="8" rx="3" ry="6.5"/><path d="M1.5 8h13M2.5 4.8h11M2.5 11.2h11"/></svg>
      <span>www.<span class="web-host">birchfieldmortgage</span>.example</span>
    </li>
    <li class="address">
      <svg viewBox="0 0 12 16"><path d="M6 0a6 6 0 0 0-6 6c0 4.5 6 10 6 10s6-5.5 6-10a6 6 0 0 0-6-6zm0 8.5A2.5 2.5 0 1 1 6 3.5a2.5 2.5 0 0 1 0 5z" fill-rule="evenodd"/></svg>
      18 Elm Ave. Alder Bay, NJ 08512
    </li>
  </ul>
</section>

</body>
</html>
```